Redesign of Real Estate Agency Website

We need a redesign for our real estate agency website. Please see attached creative brief.

Target Market(s)

Refer to creative brief.

Industry/Entity Type

Real Estate

Requirements
Must have
• Refer to creative brief.

```html
<!DOCTYPE html>
<html lang="en">
<head>
<meta charset="utf-8">
<title>CoralBay.net — Island Property and Real Estate</title>
<link rel="stylesheet" href="https://fonts.googleapis.com/css2?family=Arimo:wght@400;700&display=swap">
<style>
:root{
  --navy:#1d3a5c;
  --navy-deep:#16304d;
  --footer:#2d4a6b;
  --cream:#f4f1e8;
  --panel:#e6e0cf;
  --panel-dark:#d8d0b8;
  --panel-tag:#b5a986;
  --sky:#2a8fd0;
  --orange:#f08a1c;
  --link:#8a3a0f;
  --cta:#a0161d;
  --text:#2a2a2a;
  --muted:#666;
  --white:#fff;
  --ribbon:#111;
}
*{box-sizing:border-box;margin:0;padding:0}
html,body{width:1200px;height:2520px;overflow:hidden}
body{font-family:"Arimo",Arial,sans-serif;color:var(--text);background:var(--cream);position:relative;font-size:14px}
.abs{position:absolute}

/* header */
.header{left:0;top:0;width:1200px;height:72px;background:var(--navy-deep)}
.brand{left:30px;top:8px;color:var(--white)}
.brand-name{font-size:34px;font-weight:700;letter-spacing:.5px;display:flex;align-items:center;gap:10px}
.brand-name .dot{width:14px;height:14px;background:var(--sky)}
.brand-tag{font-size:12px;color:#c9d6e4;margin-top:2px}
.nav{left:310px;top:46px;display:flex;font-size:13px;font-weight:700;color:var(--white)}
.nav span{padding:0 12px;border-right:1px solid #5c7896}
.nav span:last-child{border-right:0}
.cart{left:930px;top:10px;display:flex;gap:10px;align-items:flex-start}
.cart-bag{width:28px;height:32px;background:#b8272b;border-radius:3px}
.cart-lines{font-size:12px;color:var(--white);line-height:17px}
.cart-lines b{color:var(--orange)}

/* hero */
.hero{left:30px;top:80px;width:1140px;height:240px;background:linear-gradient(180deg,#6fa7d6 0%,#9cc3e2 35%,#8a7a5c 60%,#4f6b33 100%);border:3px solid var(--panel-dark)}
.search{left:858px;top:88px;width:300px;height:224px;background:rgba(70,55,30,.85);border:1px solid #a08a5a;padding:10px 14px;color:var(--white)}
.search h3{font-size:17px;font-weight:700;margin-bottom:8px}
.search .field{height:17px;background:var(--white);margin-bottom:6px;font-size:11px;color:#333;padding:1px 6px;display:flex;justify-content:space-between}
.search .field i{font-style:normal;color:#888}
.search .btn{margin:8px auto 0;width:90px;height:24px;background:var(--orange);color:var(--white);font-weight:700;font-size:13px;text-align:center;line-height:24px;border-radius:3px}
.search .adv{text-align:center;font-size:11px;margin-top:6px;color:#ffd9a8;text-decoration:underline}

/* main column */
.main{left:60px;width:780px}
h2.title{font-size:28px;font-weight:700;color:var(--navy)}
h2.title em{font-style:normal;color:var(--sky)}
.para{font-size:12px;line-height:16px;color:#333}
.more{font-size:12px;font-weight:700;color:var(--navy);margin-top:4px}

.potm{left:60px;top:550px;width:780px;height:92px;background:var(--panel);padding:8px}
.potm-photo{width:120px;height:76px;background:linear-gradient(135deg,#c99463,#6f8fae)}
.potm-info{left:140px;top:10px;font-size:11px;line-height:15px}
.potm-info b{color:var(--navy);font-size:12px}
.potm-bar{left:560px;top:12px;width:210px;height:20px;font-size:10px;color:var(--white);padding:3px 8px;background:var(--panel-tag)}
.potm-foot{left:60px;top:648px;font-size:11px;color:#333;width:780px}

.tabs{left:60px;top:690px;display:flex;gap:4px}
.tab{padding:6px 14px;font-size:13px;font-weight:700;border-radius:6px 6px 0 0;background:var(--navy);color:var(--white)}
.tab.active{background:var(--sky)}
.svc{left:60px;top:716px;width:780px;height:316px;background:var(--panel);border:1px solid var(--panel-dark);padding:12px}
.svc-photo{left:12px;top:12px;width:240px;height:150px;background:linear-gradient(180deg,#7fb8e0 0%,#cfe3ee 45%,#4fa3c4 70%,#c9b58d 100%)}
.svc-head{left:270px;top:12px;font-size:19px;color:var(--navy);letter-spacing:1px}
.svc-sub{left:270px;top:36px;font-size:12px;color:#555;font-style:italic;border-bottom:1px solid #999;width:490px;padding-bottom:3px}
.ticks{left:270px;top:60px;font-size:12px;font-weight:700;line-height:20px}
.ticks li,.bul li{list-style:none;display:flex;align-items:center;gap:6px}
.ticks svg{flex:none}
.bul{left:12px;top:170px;font-size:12px;font-weight:700;line-height:17px}
.bul li::before{content:"";width:5px;height:5px;background:var(--navy);display:inline-block}
.links{left:12px;top:226px;font-size:12px;line-height:16px;color:var(--link);text-decoration:underline;font-weight:700}

.contact{left:60px;top:1046px;width:780px}
.contact-box{left:60px;top:1084px;width:780px;height:176px;background:var(--panel)}
.contact-text{left:72px;top:1094px;width:740px;font-size:12px;font-weight:700;line-height:16px}
.contact-text li{list-style:none;display:flex;gap:6px}
.contact-text li::before{content:"";flex:none;margin-top:5px;width:5px;height:5px;background:var(--navy)}
.contact-cta{left:72px;top:1190px;width:260px;font-size:13px;font-weight:700;color:var(--cta);line-height:16px}
.team{left:380px;top:1150px;width:460px;height:110px;background:linear-gradient(180deg,#e6e0cf,#8a8f99 60%,#2f3640)}

.news{left:60px;top:1270px}
.news-box{left:60px;top:1310px;width:780px;height:62px;background:var(--white);border:1px solid #ccc}
.news-label{left:72px;top:1314px;font-size:12px;font-weight:700}
.news-input{left:72px;top:1334px;width:220px;height:20px;border:1px solid #aaa;font-size:11px;color:#999;padding:3px 6px}
.news-btn{left:300px;top:1334px;width:80px;height:20px;background:var(--orange);color:var(--white);font-size:12px;font-weight:700;text-align:center;line-height:20px;border-radius:2px}
.news-priv{left:72px;top:1358px;font-size:10px;color:var(--muted)}
.news-art{left:740px;top:1314px;width:90px;height:54px;background:linear-gradient(135deg,#f6f6f6,#c8c8c8)}

/* side */
.side-title{left:870px;top:326px;font-size:24px;font-weight:700;color:var(--navy)}
.map-radio{left:870px;top:366px;font-size:11px;display:flex;gap:40px}
.map-radio span::before{content:"";display:inline-block;width:9px;height:9px;border:1px solid #555;border-radius:50%;margin-right:4px;vertical-align:-1px}
.map{left:862px;top:384px;width:280px;height:290px;background:linear-gradient(160deg,#dfe9ef,#b8c9d4)}
.map-link{left:940px;top:678px;font-size:11px;color:var(--navy);font-weight:700;text-decoration:underline}
.award{left:858px;top:706px;width:286px;height:550px}

/* footer */
.footer{left:0;top:1395px;width:1200px;height:1125px;background:var(--footer)}
.fcol{top:1430px;width:260px;color:var(--white)}
.fcol h4{font-size:16px;font-weight:700;color:var(--orange);margin-bottom:14px}
.fcol li{list-style:none;font-size:12px;line-height:24px;font-weight:700}
.fcol h4.sub{margin-top:14px}
.copy{left:0;top:2476px;width:1200px;text-align:center;font-size:11px;color:#c9d6e4;font-weight:700}
</style>
</head>
<body>

<header class="abs header">
  <div class="abs brand">
    <div class="brand-name"><span class="dot"></span>CoralBay.net</div>
    <div class="brand-tag">Island Property and Real Estate</div>
  </div>
  <nav class="abs nav">
    <span>Home</span><span>Property for Sale</span><span>Property for Rent</span><span>List your Property</span><span>Property Buyer's Guide</span><span>About us</span><span>Contact us</span>
  </nav>
  <div class="abs cart">
    <div class="cart-bag"></div>
    <div class="cart-lines"><b>0</b> items in sales inquiry cart<br><b>0</b> items in rentals inquiry cart</div>
  </div>
</header>

<div class="abs hero" role="img" aria-label="Photo of a large stone family house with lawn under blue sky"></div>
<form class="abs search">
  <h3>Quick Property Search</h3>
  <div class="field">Buy Property<i>▾</i></div>
  <div class="field">Property Type<i>▾</i></div>
  <div class="field">Region<i>▾</i></div>
  <div class="field">District<i>▾</i></div>
  <div class="field">Min Bedrooms<i>▾</i></div>
  <div class="field">Max Price (THB)<i>▾</i></div>
  <div class="btn">Search</div>
  <div class="adv">Advanced Search</div>
</form>

<h2 class="abs title main" style="top:326px">Welcome To <em>CoralBay.net</em></h2>
<div class="abs main" style="top:362px">
  <p class="para">Finding your place on the island starts here. Our team lists villas, condominiums, land and townhouses across every district, from quiet hillside retreats to homes a short walk from the beach. Every listing is checked, photographed and described with clear prices so you can compare with confidence. Whether you want to buy a holiday home, invest in a rental unit or find a long term family house, we guide you through each step, from the first viewing to the transfer of title. Browse our latest properties for sale and for rent, save favourites to your inquiry cart and contact our local agents at any time. We speak your language and know the island well, so you can focus on choosing the home that suits your life.</p>
  <div class="more">» read more</div>
</div>

<h2 class="abs title main" style="top:506px">Property of the Month</h2>
<div class="abs potm">
  <div class="potm-photo" role="img" aria-label="Photo of a pool villa terrace"></div>
  <div class="abs potm-info"><b>Palm Court Homes</b><br>Type: Garden Home<br>Price: 9,500,000 THB<br>Location: South, West Coast<br>View more</div>
  <div class="abs potm-bar">Featured this month · view details</div>
</div>
<p class="abs potm-foot">A calm garden home close to shops, schools and the west coast beaches, ready to move in. <u>View listing</u></p>

<div class="abs tabs"><span class="tab">Property for Sale</span><span class="tab active">Property for Rent</span></div>
<section class="abs svc">
  <div class="abs svc-photo" role="img" aria-label="Photo of a villa with swimming pool and garden"></div>
  <div class="abs svc-head">The Services We Offer</div>
  <div class="abs svc-sub">Comprehensive service with integrity</div>
  <ul class="abs ticks">
    <li><svg width="14" height="14" viewBox="0 0 14 14"><path d="M2 7l3 3 7-8" stroke="#1d3a5c" stroke-width="2.4" fill="none"/></svg>Extensive selection of listed properties for sale and rent.</li>
    <li><svg width="14" height="14" viewBox="0 0 14 14"><path d="M2 7l3 3 7-8" stroke="#1d3a5c" stroke-width="2.4" fill="none"/></svg>Research and suggested properties that meet client needs.</li>
    <li><svg width="14" height="14" viewBox="0 0 14 14"><path d="M2 7l3 3 7-8" stroke="#1d3a5c" stroke-width="2.4" fill="none"/></svg>Arrange property visits and viewing schedules.</li>
    <li><svg width="14" height="14" viewBox="0 0 14 14"><path d="M2 7l3 3 7-8" stroke="#1d3a5c" stroke-width="2.4" fill="none"/></svg>Guide the client through the whole purchase process.</li>
    <li><svg width="14" height="14" viewBox="0 0 14 14"><path d="M2 7l3 3 7-8" stroke="#1d3a5c" stroke-width="2.4" fill="none"/></svg>Support clients after the sale with local services.</li>
  </ul>
  <ul class="abs bul">
    <li>Offer clear legal information and assistance with property purchase.</li>
    <li>Provide transparent and competitive pricing for buyers and sellers.</li>
    <li>Provide the best possible exposure for your listing with wide marketing.</li>
  </ul>
  <div class="abs links">Property Buyer's Guide<br>Search properties for sale in the area<br>Search properties for rent in the area<br>List your property with us<br>Contact us</div>
</section>

<h2 class="abs title contact">We look forward to hearing from you!</h2>
<div class="abs contact-box"></div>
<ul class="abs contact-text">
  <li>Please look through our website to view our range of properties, or please feel free to contact us if you have any specific requirements and we will make suggestions based on your wishes.</li>
  <li>We will do our utmost to make sure your experience in buying or renting real estate on the island is exciting and pleasurable.</li>
</ul>
<p class="abs contact-cta">We at CoralBay.net Real Estate Look Forward to Finding the Ideal Island Property for You!</p>
<div class="abs team" role="img" aria-label="Photo of the real estate agency team standing together"></div>

<h2 class="abs title news">Get Our Newsletter</h2>
<div class="abs news-box"></div>
<div class="abs news-label">Get the latest CoralBay Real Estate news and updates every month</div>
<div class="abs news-input">Your Email Here ...</div>
<div class="abs news-btn">Subscribe</div>
<div class="abs news-priv">Privacy by SafeList</div>
<div class="abs news-art" role="img" aria-label="Illustration of a pen writing on paper"></div>

<h2 class="abs side-title">Search by Map</h2>
<div class="abs map-radio"><span>Buy</span><span>Rent</span></div>
<div class="abs map" role="img" aria-label="Map of the island divided into north, east, west, south and town districts"></div>
<div class="abs map-link">View large map</div>
<svg class="abs award" viewBox="0 0 286 550" aria-hidden="true">
  <rect x="0" y="0" width="286" height="16" fill="#a0161d"/>
  <path d="M0 16H286V550L143 500L0 550Z" fill="#111"/>
</svg>

<footer class="abs footer"></footer>
<div class="abs fcol" style="left:50px">
  <h4>Island Real Estate for Sale</h4>
  <ul><li>island property for sale</li><li>condo property for sale</li><li>apartments for sale</li><li>villas and houses for sale</li><li>land for sale</li><li>commercial property for sale</li><li>luxury property for sale</li><li>property on the beach</li><li>property buyer's guide</li><li>new projects</li><li>property on sea view</li><li>property for families</li><li>land offers</li><li>town units</li><li>property list</li></ul>
</div>
<div class="abs fcol" style="left:345px">
  <h4>Island Property for Rent</h4>
  <ul><li>island property for rent</li><li>condo property for rent</li><li>property holiday rentals</li><li>· holiday villas</li><li>· luxury villas</li><li>· cheap villas</li><li>· holiday apartments</li><li>· holiday condos</li><li>· holiday units</li><li>· town houses</li><li>· week rentals</li><li>property long rent</li><li>· long term houses</li><li>· long term apartments</li><li>property rent guide</li></ul>
</div>
<div class="abs fcol" style="left:640px">
  <h4>Site Links</h4>
  <ul><li>property and services</li><li>privacy policy</li><li>disclaimer</li><li>site map</li></ul>
  <h4 class="sub">About CoralBay.net Real Estate</h4>
  <ul><li>about us</li><li>contact us</li><li>list your property</li><li>· selling your property</li></ul>
</div>
<div class="abs fcol" style="left:935px">
  <h4>Island Info</h4>
  <ul><li>island information</li><li>districts</li><li>news</li><li>dining / nightlife</li><li>events</li><li>shopping</li><li>attractions</li><li>hotels</li></ul>
</div>
<p class="abs copy">CoralBay.net Real Estate · Copyright © CoralBay.net · All Rights Reserved.</p>

</body>
</html>
```